Postcard Design

Domestic home cleaning business.......looking to call it " copper lantern" I would like to have a vastrelo bottle as the main feature.....on the bottle the centre lable shoild read I'M YOUR ALL PURPOSE CLEANER above the lable should read DON'T LIFT A FINGER! Then opposite the bottle 5 bullet points House Keeping, Washing,Ironing bed changing, END OF TENANCY CLEANS, MOVING IN CLEANS spring cleans.

On the back of the card Iwould like to list the following: At the top of the card it should read
THE ALL PURPOSE PERSONALISED CLEANER AND WHAT YOU CAN EXPECT

Reliable
Police checked and referenced cleaners
SAME CLEANER EVERY WEEK ON THE SAME DAY AND TIME TO BE AGREED BY YOU
ONLY EVER USE CUSTOMERS OWN PRODUCTS
EACH CLEAN INSURED
GENERAL HOUSE CLEANING AS WELL AS IRONING IF REQUIRED (min 2hours per week)

Reason: I have a couple of hospital appointments to attend this week after s major operation, so I need more time to concentrate......sorry

```html
<!DOCTYPE html>
<html lang="en">
<head>
<meta charset="utf-8">
<title>Copper Lantern – Postcard Back</title>
<link href="https://fonts.googleapis.com/css2?family=Arimo:wght@400;700&display=swap" rel="stylesheet">
<style>
  :root {
    --blue-deep: #0062ad;
    --blue-mid: #1a8fd6;
    --blue-light: #bfe0f5;
    --white: #ffffff;
    --yellow: #fff200;
    --green: #22ad4f;
    --ink: #111111;
  }
  html, body {
    margin: 0;
    padding: 0;
    overflow: hidden;
    background: var(--white);
  }
  .postcard {
    position: relative;
    width: 1200px;
    height: 930px;
    overflow: hidden;
    font-family: "Arimo", Helvetica, Arial, sans-serif;
    background:
      radial-gradient(ellipse 620px 560px at 880px 560px, var(--white) 55%, rgba(255,255,255,0) 100%),
      radial-gradient(ellipse 520px 420px at 330px 860px, var(--white) 40%, rgba(255,255,255,0) 100%),
      linear-gradient(120deg, var(--blue-deep) 0%, #0a78c4 30%, var(--blue-mid) 45%, var(--blue-light) 62%, var(--white) 75%);
  }
  .postcard__swirls {
    position: absolute;
    inset: 0;
  }
  .brand {
    position: absolute;
    left: 62px;
    top: 146px;
    width: 168px;
    display: flex;
    align-items: center;
    gap: 10px;
  }
  .brand__dot {
    flex: none;
    width: 18px;
    height: 18px;
    border-radius: 50%;
    background: var(--white);
  }
  .brand__name {
    color: var(--white);
    font-weight: 700;
    font-size: 26px;
    line-height: 28px;
    text-transform: uppercase;
    letter-spacing: -0.5px;
  }
  .headline {
    position: absolute;
    left: 246px;
    top: 88px;
    margin: 0;
    color: var(--yellow);
    font-weight: 700;
    font-size: 35px;
    line-height: 32px;
    letter-spacing: -0.3px;
    text-transform: uppercase;
  }
  .promise {
    position: absolute;
    left: 63px;
    top: 300px;
    margin: 0;
  }
  .promise__title {
    margin: 0 0 2px;
    color: var(--yellow);
    font-weight: 700;
    font-size: 23px;
    line-height: 30px;
    text-transform: uppercase;
  }
  .promise__list {
    list-style: none;
    margin: 0;
    padding: 0;
    color: var(--white);
    font-size: 24px;
    line-height: 30.4px;
    letter-spacing: -0.1px;
  }
  .mail-label {
    position: absolute;
    margin: 0;
    color: var(--green);
    font-size: 33px;
    line-height: 40px;
    letter-spacing: -1.4px;
    font-weight: 400;
  }
  .mail-label--postage {
    left: 968px;
    top: 108px;
    text-align: center;
    width: 120px;
  }
  .mail-label--address {
    left: 640px;
    top: 373px;
  }
  .mail-label--barcode {
    left: 522px;
    top: 814px;
  }
  .address-line {
    position: absolute;
    left: 640px;
    top: 416px;
    margin: 0;
    color: var(--ink);
    font-size: 25px;
    line-height: 30px;
    letter-spacing: -0.8px;
  }
</style>
</head>
<body>
<main class="postcard">
  <svg class="postcard__swirls" width="1200" height="930" viewBox="0 0 1200 930" aria-hidden="true">
    <g fill="none" stroke="#ffffff">
      <circle cx="960" cy="170" r="390" stroke-opacity="0.35" stroke-width="2"/>
      <circle cx="1100" cy="150" r="270" fill="#ffffff" fill-opacity="0.35" stroke-opacity="0"/>
      <circle cx="820" cy="640" r="360" stroke-opacity="0.3" stroke-width="2"/>
      <circle cx="640" cy="660" r="360" stroke-opacity="0.25" stroke-width="2"/>
      <circle cx="300" cy="1050" r="420" fill="#ffffff" fill-opacity="0.3" stroke-opacity="0"/>
      <circle cx="1120" cy="760" r="330" fill="#ffffff" fill-opacity="0.4" stroke-opacity="0"/>
    </g>
  </svg>

  <div class="brand">
    <span class="brand__dot"></span>
    <span class="brand__name">Copper<br>Lantern</span>
  </div>

  <h1 class="headline">The all purpose<br>personalised<br>cleaner and<br>what you<br>can expect</h1>

  <section class="promise">
    <h2 class="promise__title">Reliable</h2>
    <ul class="promise__list">
      <li>Police checked and referenced cleaners</li>
      <li>Same cleaner every week on the same<br>day and time to be agreed by you</li>
      <li>Only ever use customers own products</li>
      <li>Each clean insured</li>
      <li>General house cleaning as well as<br>ironing if required (min 2hours per week)</li>
    </ul>
  </section>

  <p class="mail-label mail-label--postage">Postage Area</p>
  <p class="mail-label mail-label--address">Address area</p>
  <p class="address-line">Address area</p>
  <p class="mail-label mail-label--barcode">Barcode area</p>
</main>
</body>
</html>
```